Custom unique Stationary design for Logistics company

We need a custom, unique , elegant and luxurious full stationary design using our new logo, following these guidelines:
1- Business card: double sided, both sides uses the navy blue as the background main color (same as the code of the navy blue used in our logo).
2- envelope and folder: also use the same navy blue as the main background color.
3- book cover( notepad cover) : same thing with the navy blue
4- letterhead: feel free to use the combination of the colors in our logo.
5- rest of the items are up to your creativity

Target Market(s)

corporates and other businesses

Industry/Entity Type

Logistics and heavy machines contractors

Requirements
Must have
• Letterhead, business card, envelope, notepad cover, paper, file
Nice to have
• navy blue to be main background color for business card, envelope, notepad cover

```html
<!DOCTYPE html>
<html lang="en">
<head>
<meta charset="utf-8">
<title>Meridian Freight Group – Stationery</title>
<link href="https://fonts.googleapis.com/css2?family=Open+Sans:wght@400;600&family=Roboto:wght@400;500;700&display=swap" rel="stylesheet">
<style>
  :root{
    --navy:#1f5a7a;
    --navy-deep:#1a4f6c;
    --orange:#e0622f;
    --paper:#f3f3f3;
    --ground:#e6e6e6;
    --ink:#3d3d3d;
    --grey:#555;
    --photo-light:#b9d3e6;
    --photo-mid:#5f90bd;
    --photo-dark:#2a5a8a;
  }
  *{box-sizing:border-box;margin:0;padding:0}
  html,body{width:1200px;height:795px;overflow:hidden;background:var(--ground)}
  .canvas{position:relative;width:1200px;height:795px;font-family:"Roboto",sans-serif}
  .sheet{position:absolute;background:var(--paper)}
  .brand{display:flex;align-items:center;gap:4px;color:var(--navy);font-family:"Roboto",sans-serif;font-weight:700;white-space:nowrap;justify-content:center}
  .brand-dot{border-radius:50%;background:var(--orange);flex:none}
  .brand.on-navy{color:#fff}
  address{font-style:normal}

  /* Letterhead */
  .letterhead{left:292px;top:99px;width:293px;height:415px}
  .letterhead .brand{position:absolute;top:30px;left:0;right:0;font-size:13px}
  .letterhead .brand-dot{width:7px;height:7px}
  .letter-body{position:absolute;left:26px;right:27px;top:100px;font-family:"Open Sans",sans-serif;font-size:4.85px;line-height:8px;color:var(--ink);text-align:justify}
  .letter-body p{margin-bottom:8px}
  .signature{position:absolute;left:27px;top:310px;width:36px;height:32px}
  .letter-footer{position:absolute;left:26px;right:27px;top:367px;display:flex;justify-content:space-between;font-size:6.6px;line-height:8.6px;color:var(--grey)}
  .contact-list{list-style:none}
  .contact-list li{display:flex;align-items:center;gap:3px}
  .contact-list svg{width:6px;height:6px;flex:none}
  .address{text-align:right}

  /* Folder */
  .folder{left:637px;top:80px;width:345px;height:436px}
  .folder-spine{position:absolute;left:0;top:0;bottom:0;width:19px;border-right:1px solid #d8d8d8}
  .folder-spine::before{content:"";position:absolute;left:6px;top:0;bottom:0;border-left:1px solid #dcdcdc}
  .folder .brand{position:absolute;top:46px;left:19px;right:0;font-size:25px;gap:7px}
  .folder .brand-dot{width:12px;height:12px}
  .folder-band-top{position:absolute;left:0;right:0;top:123px;height:4px;background:var(--navy)}
  .folder-photo{position:absolute;left:0;right:0;top:127px;height:243px;background:linear-gradient(180deg,var(--photo-light) 0%,var(--photo-mid) 50%,var(--photo-dark) 100%)}
  .folder-band-bottom{position:absolute;left:0;right:0;top:370px;height:4px;background:var(--orange)}
  .folder-info{position:absolute;left:19px;right:0;top:390px;text-align:center;font-size:7.6px;line-height:9.4px;color:var(--grey)}
  .folder-info .name{color:var(--navy);font-weight:500}
  .folder-info .web b{color:var(--navy);font-weight:500}

  /* Business cards */
  .card{position:absolute;left:187px;width:132px;height:75px;background:var(--navy)}
  .card-front{top:551px}
  .card-front .brand{position:absolute;top:26px;left:0;right:0;font-size:11px}
  .card-front .brand-dot{width:6px;height:6px}
  .card-back{top:646px}
  .card-back .brand{position:absolute;top:13px;right:12px;font-size:7px;gap:2px}
  .card-back .brand-dot{width:4px;height:4px}
  .person{position:absolute;left:10px;top:37px;font-size:4px;line-height:4.6px;color:#fff}
  .person .name{color:var(--orange);font-weight:700;text-transform:uppercase}
  .card-foot{position:absolute;left:10px;right:11px;bottom:8px;display:flex;justify-content:space-between;font-size:3.3px;line-height:4.4px;color:#fff}
  .card-foot .contact-list svg{width:3px;height:3px}

  /* Envelopes */
  .envelope{top:561px;width:329px;height:157px}
  .envelope-front{left:353px}
  .envelope-front .brand{position:absolute;top:33px;left:24px;font-size:11px;justify-content:flex-start}
  .envelope-front .brand-dot{width:6px;height:6px}
  .sender{position:absolute;left:23px;top:112px;font-size:6.1px;line-height:7.6px;color:var(--grey)}
  .sender .name{color:var(--navy);font-weight:500}
  .envelope-back{left:713px}
  .envelope-flap{position:absolute;left:0;right:0;top:0;height:56px;background:var(--navy);clip-path:polygon(0 0,100% 0,98% 100%,2% 100%)}
  .envelope-flap .brand{position:absolute;top:22px;left:0;right:0;font-size:10px}
  .envelope-flap .brand-dot{width:5px;height:5px}
</style>
</head>
<body>
<main class="canvas">

  <section class="sheet letterhead">
    <div class="brand"><span class="brand-dot"></span>Meridian Freight Group</div>
    <div class="letter-body">
      <p>Dear customer,</p>
      <p>Lorem ipsum dolor sit amet, consectetur adipisicing elit, sed do eiusmod tempor incididunt ut labore et dolore magna aliqua. Ut enim ad minim veniam, quis nostrud exercitation ullamco laboris nisi ut aliquip ex ea commodo consequat. Duis aute irure dolor in reprehenderit in voluptate velit esse cillum dolore eu fugiat nulla pariatur. Excepteur sint occaecat cupidatat non proident, sunt in culpa qui officia deserunt mollit anim id est laborum.</p>
      <p>Lorem ipsum dolor sit amet, consectetur adipisicing elit, sed do eiusmod tempor incididunt ut labore et dolore magna aliqua. Ut enim ad minim veniam, quis nostrud exercitation ullamco laboris nisi ut aliquip ex ea commodo consequat. Duis aute irure dolor in reprehenderit in voluptate velit esse cillum dolore eu fugiat nulla pariatur. Excepteur sint occaecat cupidatat non proident, sunt in culpa qui officia deserunt mollit anim id est laborum.</p>
      <p>Lorem ipsum dolor sit amet, consectetur adipisicing elit, sed do eiusmod tempor incididunt ut labore et dolore magna aliqua. Ut enim ad minim veniam, quis nostrud exercitation ullamco laboris nisi ut aliquip ex ea commodo consequat. Duis aute irure dolor in reprehenderit in voluptate velit esse cillum dolore eu fugiat nulla pariatur. Excepteur sint occaecat cupidatat non proident, sunt in culpa qui officia deserunt mollit anim id est laborum.</p>
      <p>Lorem ipsum dolor sit amet, consectetur adipisicing elit, sed do eiusmod tempor incididunt ut labore et dolore magna aliqua. Ut enim ad minim veniam, quis nostrud exercitation ullamco laboris nisi ut aliquip ex ea commodo consequat. Duis aute irure dolor in reprehenderit.</p>
      <p>Yours Sincerely,</p>
    </div>
    <svg class="signature" role="img" aria-label="Handwritten signature" viewBox="0 0 36 32"><rect width="36" height="32" fill="#e4e4e4"/></svg>
    <footer class="letter-footer">
      <ul class="contact-list">
        <li><svg viewBox="0 0 10 10"><path d="M2 1l2 2-1 1.5c.8 1.5 1.5 2.2 3 3L7.5 6l2 2-1.5 1.5C4 9 1 6 .5 2z" fill="var(--orange)"/></svg>555-010-2231</li>
        <li><svg viewBox="0 0 10 10"><rect x="0.5" y="2" width="9" height="6.5" fill="var(--orange)"/><path d="M.5 2l4.5 3.5L9.5 2" stroke="#fff" fill="none" stroke-width=".8"/></svg>info@meridianfreight.com</li>
        <li><svg viewBox="0 0 10 10"><circle cx="5" cy="5" r="4.2" fill="none" stroke="var(--orange)" stroke-width="1.2"/></svg>www.meridianfreight.com</li>
      </ul>
      <address class="address">Meridian Freight Group<br>48 Harbour Line Drive<br>Portvale, ON K0A 1B2</address>
    </footer>
  </section>

  <section class="sheet folder">
    <div class="folder-spine"></div>
    <div class="brand"><span class="brand-dot"></span>Meridian Freight</div>
    <div class="folder-band-top"></div>
    <div class="folder-photo" role="img" aria-label="Photo of a container ship with cranes in a harbour on blue water"></div>
    <div class="folder-band-bottom"></div>
    <div class="folder-info">
      <div class="name">Meridian Freight Group</div>
      <div>Quay St. 48 Harbour Line Drive Portvale, ON K0A 1B2</div>
      <div class="web">www.<b>meridianfreight</b>.com</div>
    </div>
  </section>

  <section class="card card-front">
    <div class="brand on-navy"><span class="brand-dot"></span>Meridian Freight</div>
  </section>

  <section class="card card-back">
    <div class="brand on-navy"><span class="brand-dot"></span>Meridian Freight</div>
    <div class="person"><div class="name">Daniel Hartwell</div><div>Managing Director</div></div>
    <footer class="card-foot">
      <ul class="contact-list">
        <li><svg viewBox="0 0 10 10"><circle cx="5" cy="5" r="4" fill="var(--orange)"/></svg>555-014-7720</li>
        <li><svg viewBox="0 0 10 10"><rect x="1" y="2" width="8" height="6" fill="var(--orange)"/></svg>info@meridianfreight.com</li>
        <li><svg viewBox="0 0 10 10"><circle cx="5" cy="5" r="3.6" fill="none" stroke="var(--orange)" stroke-width="1.4"/></svg>www.meridianfreight.com</li>
      </ul>
      <address class="address">Meridian Freight Group<br>12 Quay Street, Suite 300<br>Easton, WV 25000</address>
    </footer>
  </section>

  <section class="sheet envelope envelope-front">
    <div class="brand"><span class="brand-dot"></span>Meridian Freight</div>
    <address class="sender">
      <div class="name">Meridian Freight Group</div>
      <div>48 Harbour Line Drive</div>
      <div>Portvale, ON K0A 1B2</div>
    </address>
  </section>

  <section class="sheet envelope envelope-back">
    <div class="envelope-flap">
      <div class="brand on-navy"><span class="brand-dot"></span>Meridian Freight</div>
    </div>
  </section>

</main>
</body>
</html>
```